Catalogue for our Medical Products for Print

We need a wonderful catalogue design with details our products in German. Products and website see www.vortelsupply.example.

See file attached, 1 catalogue generated automatically has to be pimped and added by short description of products.

Thank you for your help. We need the products descriptions in the overview copied into the catalogue.

Target Market(s)

Doctors and hospitals, private people as well.

Font styles to use
Sans Serif

Requirements
Must have
• Nice overview of our products and categories.
Nice to have
• Our colors like website

```html
<!DOCTYPE html>
<html lang="de">
<head>
<meta charset="utf-8">
<title>Vortel Supply – Katalog</title>
<link rel="stylesheet" href="https://fonts.googleapis.com/css2?family=Roboto:wght@400;500;700&family=Oswald:wght@600&display=swap">
<style>
:root{
  --red:#e62129;
  --ink:#1d1d1b;
  --dark:#222;
  --paper:#fff;
  --stage:#a2a2a2;
  --cell-light:#ededed;
  --cell-dark:#dcdcdc;
  --rule:#9a9a9a;
}
*{box-sizing:border-box;margin:0;padding:0}
html,body{width:1200px;height:1200px;overflow:hidden}
body{background:var(--stage);position:relative;font-family:"Roboto",Arial,sans-serif;color:var(--ink)}
.page{position:absolute;width:347px;height:491px;background:var(--paper);overflow:hidden}
.page--order{left:245px;top:84px}
.page--overview{left:651px;top:84px;width:348px}
.page--extra{left:450px;top:614px}
.abs{position:absolute}
.brand{position:absolute;left:0;right:0;display:flex;justify-content:center;align-items:center;gap:6px}
.brand__mark{width:16px;height:16px;background:var(--red)}
.brand__name{font-size:17px;font-weight:500;color:var(--red);letter-spacing:-.2px}
.cat-title{position:absolute;left:0;right:0;text-align:center;top:69px;font-size:11.5px;font-weight:500}
.cat-sub{position:absolute;left:0;right:0;text-align:center;top:86px;font-size:8.5px}
.headline{position:absolute;left:0;right:0;text-align:center;top:105px;font-family:"Oswald","Arial Narrow",sans-serif;font-weight:600;font-size:16.5px;color:var(--red)}
.contact{position:absolute;left:0;top:147px;width:189px;height:91px;background:var(--red);color:#fff;padding:8px 0 0 31px;font-size:5.4px;line-height:7.4px}
.contact__title{font-size:8.5px;font-weight:500;margin-bottom:3px;line-height:10px}
.contact b{font-weight:700}
.portrait{position:absolute;left:108px;top:145px;width:81px;height:93px;background:linear-gradient(180deg,#d6a56f 0%,#eac8a8 40%,#f4f4f4 70%,#ffffff 100%)}
.namebar{position:absolute;left:0;top:238px;width:189px;height:12px;background:var(--dark);color:#fff;font-size:6.3px;text-align:right;padding:2px 6px 0 0}
.namebar::before{content:"";position:absolute;left:31px;top:6px;width:80px;height:.5px;background:#fff}
.orderhead{position:absolute;left:198px;top:178px;font-size:11px;font-weight:500;line-height:13.5px}
.orderhead span{display:block;font-size:9.5px;font-weight:700}
.field{position:absolute;left:32px;right:32px;font-size:5.4px;display:flex;align-items:flex-end;gap:4px}
.field i{flex:1;border-bottom:.5px solid var(--rule);height:1px}
.question{position:absolute;left:32px;top:349px;font-size:5.6px;font-weight:700}
.line{position:absolute;left:32px;right:32px;border-bottom:.5px solid var(--rule)}
.footer{position:absolute;left:0;right:0;height:31px;background:var(--red);color:#fff;font-size:5.4px;line-height:8px;text-align:center;padding-top:7px}
.footer b{font-weight:700}
.item{position:absolute;font-size:5.4px;line-height:6.3px}
.item h3{font-size:7px;font-weight:700;margin-bottom:2px;line-height:8px}
.item p{margin-bottom:3px}
.thumb{position:absolute}
.divider{position:absolute;left:193px;top:114px;height:150px;border-left:.5px solid var(--rule)}
.cell{position:absolute;height:62px;width:123px}
.cell--l{left:32px;width:161px}
.cell--r{left:193px}
.light{background:var(--cell-light)}
.darker{background:var(--cell-dark)}
.extra-item{position:absolute;left:156px;font-size:5.4px;line-height:7.4px}
.extra-item h3{font-size:8px;font-weight:400;margin-bottom:2px}
</style>
</head>
<body>

<section class="page page--order">
  <div class="brand" style="top:28px"><span class="brand__mark"></span><span class="brand__name">Vortel Supply</span></div>
  <h1 class="cat-title">vortelsupply.example catalog</h1>
  <p class="cat-sub">This catalog was generated on 18. November</p>
  <h2 class="headline">VORTEL SUPPLY GMBH - KATALOG</h2>

  <div class="contact">
    <div class="contact__title">KONTAKT</div>
    Vortel Supply GmbH<br>Lindenweg 12<br>6020 Talheim<br>
    <div style="height:5px"></div>
    www.<b>vortelsupply</b>.example<br>Kostenlose 24h Hotline:<br>+43 800 00 00 11<br>FAX: +43 512 000 000 145
  </div>
  <div class="portrait" role="img" aria-label="Foto einer Mitarbeiterin im weißen Hemd"></div>
  <div class="namebar">Lena Hartwig,B.sc.</div>

  <div class="orderhead">BESTELLFORMULAR<span>FAX: +43 512 000 000 145</span></div>

  <div class="field" style="top:270px">NAME: <i></i></div>
  <div class="field" style="top:285px">Anschrift: <i></i></div>
  <div class="field" style="top:300px">Email tur Bestellbestätigung: <i></i></div>
  <div class="field" style="top:315px">Telefone (Optional) für Rückfragen: <i></i></div>

  <p class="question">Welche Produkte wollen bestellen?</p>
  <div class="line" style="top:375px"></div>
  <div class="line" style="top:395px"></div>
  <div class="line" style="top:416px"></div>

  <footer class="footer" style="top:450px">Ich akzeptiere die AGBs und die Datenschuzvereinbarung. Diese finden Sie online aut<br>www.<b>vortelsupply</b>.example FAX: +43 512 000 000 1454</footer>
</section>

<section class="page page--overview">
  <div class="brand" style="top:28px"><span class="brand__mark"></span><span class="brand__name">Vortel Supply</span></div>
  <h1 class="cat-title">vortelsupply.example catalog</h1>
  <p class="cat-sub">This catalog was generated on 18. November</p>

  <div class="thumb" role="img" aria-label="Gelber Entsorgungsbehälter" style="left:33px;top:114px;width:26px;height:38px;background:linear-gradient(#d8333a 0 18%,#f3d24a 18%)"></div>
  <div class="item" style="left:77px;top:116px"><h3>Abfallbehälter</h3><p>SafeBin Duo Entsorgungsbehälter</p><p>2,26 € – 6,73 € exkl. MwSt.</p></div>

  <div class="thumb" role="img" aria-label="Absaugpumpe" style="left:34px;top:167px;width:30px;height:27px;background:linear-gradient(#dcdcdc,#b8b8b8 60%,#d0383d 60%)"></div>
  <div class="item" style="left:77px;top:165px"><h3>Absaugpumpe</h3><p>Velmar Suctio Absaugpumpe Pro</p><p>1.149,00 € exkl. MwSt.</p></div>

  <div class="thumb" role="img" aria-label="Mehrwegbeutel mit Schlauch" style="left:34px;top:215px;width:30px;height:32px;background:linear-gradient(#f2f2f2,#d8dde2)"></div>
  <div class="item" style="left:77px;top:213px"><h3>Absaugpumpe</h3><p>Velmar Suctio Mehrwegbeutel<br>und Absaugschlauch</p><p>150,00 € exkl. MwSt.</p></div>

  <div class="divider"></div>

  <div class="thumb" role="img" aria-label="Absaugpumpe kompakt" style="left:206px;top:113px;width:32px;height:30px;background:linear-gradient(#e6e6e6,#a9a9a9)"></div>
  <div class="item" style="left:249px;top:114px"><h3>Absaugpumpe</h3><p>Velmar Suctio<br>AbsaugpumpeLite</p><p>769,00 € – 799,00 € exkl.</p></div>

  <div class="thumb" role="img" aria-label="Einwegbehälter" style="left:207px;top:163px;width:28px;height:28px;background:linear-gradient(#eef5f6,#cfe1e5)"></div>
  <div class="item" style="left:250px;top:164px"><h3>Absaugpumpe</h3><p>Velmar Suctio<br>Einwegbehälter<br>und Absaugschlauch</p><p>280,00 € exkl. MwSt.</p></div>

  <div class="thumb" role="img" aria-label="Absaugkatheter" style="left:208px;top:214px;width:28px;height:30px;background:linear-gradient(135deg,#fff,#e4e4e4)"></div>
  <div class="item" style="left:249px;top:213px"><h3>Absaugpumpe</h3><p>Absaugkatheter für die<br>Tracheobronchiale<br>Absaugung</p><p>9,00 € exkl. MwSt.</p></div>

  <div class="cell cell--l light" style="top:271px;height:61px"></div>
  <div class="cell cell--r darker" style="top:271px;height:61px"></div>
  <div class="cell cell--l darker" style="top:332px"></div>
  <div class="cell cell--r light" style="top:332px"></div>
  <div class="cell cell--l light" style="top:394px;height:58px"></div>
  <div class="cell cell--r darker" style="top:394px;height:58px"></div>

  <div class="thumb" role="img" aria-label="Ampullarium Tasche" style="left:39px;top:280px;width:28px;height:36px;background:linear-gradient(#3a3a3a,#1e1e1e)"></div>
  <div class="item" style="left:77px;top:283px"><h3>Ampullarium</h3><p>CarryMed Vial Ampullarium</p><p>29,17 € exkl. MwSt.</p></div>

  <div class="thumb" role="img" aria-label="Rote Ampullarium Tasche" style="left:203px;top:280px;width:34px;height:38px;background:linear-gradient(#e04049,#b3262c)"></div>
  <div class="item" style="left:249px;top:282px"><h3>Ampullarium</h3><p>Rettra Ampullarium<br>Größe L</p><p>99,17 € exkl. MwSt.</p></div>

  <div class="thumb" role="img" aria-label="Knochenbohrer" style="left:40px;top:345px;width:28px;height:28px;background:linear-gradient(135deg,#e9e9e9,#b23a3a)"></div>
  <div class="item" style="left:77px;top:341px"><h3>Ausgewählte Produkte</h3><p>Knochenbohrer OssPort G3 für den<br>intraossären Zugang</p><p>307,50 € – 1.082,50 € exkl.</p></div>

  <div class="thumb" role="img" aria-label="Beatmungsbeutel" style="left:205px;top:345px;width:30px;height:26px;background:linear-gradient(90deg,#2a66c9,#6fa4e6)"></div>
  <div class="item" style="left:249px;top:336px"><h3>Ausgewählte<br>Produkte</h3><p>Breva Mark IV-Beat-<br>mungsbeutel für<br>Erwachsene</p><p>162,50 – 237,50<br>exkl. MwSt.</p></div>

  <div class="thumb" role="img" aria-label="Pulsoximeter Set" style="left:36px;top:403px;width:34px;height:30px;background:linear-gradient(135deg,#f4f4f4,#9fb4cc)"></div>
  <div class="item" style="left:77px;top:406px"><h3>Ausgewählte Produkte</h3><p>PulseSign S Pulsoximeter Set</p><p>499,17 exkl. MwSt.</p></div>

  <div class="thumb" role="img" aria-label="Videolaryngoskop" style="left:210px;top:403px;width:20px;height:38px;background:linear-gradient(#5b5b5b,#c9c9c9)"></div>
  <div class="item" style="left:249px;top:400px"><h3>Ausgewählte<br>Produkte</h3><p>Videolaryngoskop<br>ClearView MAC</p><p>1.829,00 € – 8.145,00<br>€ exkl. MwSt.</p></div>

  <footer class="footer" style="top:452px">Ich akzeptiere die AGBs und die Datenschuzvereinbarung. Diese finden Sie online aut<br>www.<b>vortelsupply</b>.example FAX: +43 512 000 000 1454</footer>
</section>

<section class="page page--extra">
  <div class="brand" style="top:128px"><span class="brand__mark"></span><span class="brand__name">Vortel Supply</span></div>

  <div class="thumb" role="img" aria-label="Wundverschlussstreifen" style="left:84px;top:191px;width:44px;height:52px;background:linear-gradient(135deg,#f2f4f3,#c9d3cf)"></div>
  <div class="extra-item" style="top:209px">Closafix Wundverschlussstreifen<br>46,33 £ - 88, 11 £ exwl.Mwst</div>

  <div class="thumb" role="img" aria-label="Zahnschiene" style="left:74px;top:268px;width:64px;height:45px;background:linear-gradient(135deg,#c9c9d4,#7d86b3)"></div>
  <div class="extra-item" style="top:268px"><h3>Zahnmesizin</h3>Hydrosplint Hydrostatische Schiene - Soforthilife bei CMD -<br>Beschwerden - BeiBschience<br><span style="display:block;height:7px"></span>21,90 £ exld,MwSt.</div>

  <footer class="footer" style="top:450px">Ich akzeptiere die AGBs und die Datenschuzvereinbarung. Diese finden Sie online aut<br>www.<b>vortelsupply</b>.example FAX: +43 512 000 000 1454</footer>
</section>

</body>
</html>
```